Optometrist/Eye Care Clinic Business card with new logo attached

We are a small, independent eye care clinic in Canada. We have recently updated our logo (as attached), and would like a professional, modern and health care oriented business card to highlight our office details and our optometrist. We'd like to incorporate the blue colours as seen on our logo.

Target Market(s)

demographic: age 35-65 male/female equal

Industry/Entity Type

Health Care

Contact Information for Business Card

Name of clinic: "Marrow Bend Eye Care Optometry"

Font styles to use
Sans Serif

Colors
0355a3

Requirements
Must have
• our website: marrowbendeyecare.com
• Dr Lena Quorvik
• Optometrist
• 217-392 E Halvering Ave
• Vancouver BC V6R 3J8
• P: 604-319-2058
• E: info@marrowbendeyecare.com
Nice to have
• front side: logo/name of clinic as seen on logo attached and website
• backside: logo on the left side, and name/title/address/phone/email

```html
<!DOCTYPE html>
<html lang="en">
<head>
<meta charset="utf-8">
<title>Marrow Bend Eye Care Optometry – Business Card</title>
<link href="https://fonts.googleapis.com/css2?family=Montserrat:wght@700&family=Questrial&family=Open+Sans:wght@400&display=swap" rel="stylesheet">
<style>
  :root {
    --canvas: #b9b9b9;
    --card-white: #ffffff;
    --brand-blue: #0355a3;
    --navy: #0b3f63;
    --teal: #1a86b3;
    --ink: #1d2a36;
    --rule: #d4d8dc;
    --emboss: #0f4d74;
  }
  * { box-sizing: border-box; margin: 0; padding: 0; }
  html, body {
    width: 1200px; height: 1138px; overflow: hidden;
    background: var(--canvas);
  }
  .card {
    position: absolute;
    width: 730px; height: 414px;
    overflow: hidden;
  }
  .card--front { left: 235px; top: 160px; background: var(--card-white); }
  .card--back  { left: 235px; top: 600px; background: var(--brand-blue); }

  /* wordmark */
  .wordmark {
    position: absolute;
    display: flex; flex-direction: column; align-items: center;
    font-family: "Questrial", sans-serif;
    letter-spacing: 0.22em;
    font-size: 27px; line-height: 1.3;
    text-align: center;
  }
  .wordmark__dot {
    width: 130px; height: 130px; border-radius: 50%;
    margin-bottom: 18px;
  }
  .card--front .wordmark { left: 56px; top: 70px; width: 290px; color: var(--teal); }
  .card--front .wordmark__dot { background: var(--navy); }
  .card--back .wordmark { left: 190px; top: 60px; width: 350px; color: var(--emboss); }
  .card--back .wordmark__dot { background: var(--emboss); }

  .divider {
    position: absolute; left: 344px; top: 80px;
    width: 2px; height: 212px; background: var(--rule);
  }
  .contact {
    position: absolute; left: 372px; top: 82px;
    color: var(--ink);
  }
  .contact__name {
    font-family: "Montserrat", sans-serif; font-weight: 700;
    font-size: 24px; color: var(--navy); letter-spacing: 0.01em;
  }
  .contact__title {
    font-family: "Questrial", sans-serif;
    font-size: 22px; color: var(--teal); margin-top: 2px;
  }
  .contact__list {
    list-style: none; margin-top: 22px;
    font-family: "Open Sans", sans-serif; font-size: 18.5px; line-height: 30px;
  }
  .contact__list li { display: flex; align-items: flex-start; gap: 7px; }
  .contact__list li.gap { margin-top: 12px; }
  .contact__list svg { width: 16px; height: 16px; margin-top: 7px; flex: none; }
  .contact__address span { display: block; }

  .wave { position: absolute; left: 0; bottom: 0; width: 730px; height: 100px; }

  .website {
    position: absolute; left: 0; right: 0; top: 349px;
    text-align: center;
    font-family: "Open Sans", sans-serif; font-size: 20px;
    letter-spacing: 0.08em; color: #ffffff;
  }
</style>
</head>
<body>

<section class="card card--front" aria-label="Business card front">
  <div class="wordmark">
    <span class="wordmark__dot" aria-hidden="true"></span>
    <span>MARROW BEND</span>
    <span>EYE CARE</span>
    <span>OPTOMETRY</span>
  </div>

  <div class="divider"></div>

  <div class="contact">
    <h1 class="contact__name">DR LENA QUORVIK</h1>
    <p class="contact__title">OPTOMETRIST</p>
    <ul class="contact__list">
      <li>
        <svg viewBox="0 0 16 16" aria-hidden="true"><circle cx="8" cy="8" r="7" fill="none" stroke="#0b3f63" stroke-width="1.4"/><path d="M5.5 4.5c-.8.8-.6 3 1 4.9s3.8 2.6 4.6 1.7l-1.3-1.4-1 .6c-.7-.3-1.6-1.3-1.9-2l.6-1z" fill="#0b3f63"/></svg>
        <span>604-319-2058</span>
      </li>
      <li>
        <svg viewBox="0 0 16 16" aria-hidden="true"><path d="M1 6l7-4 7 4v8H1z" fill="#0b3f63"/><path d="M1 6l7 4.5L15 6" fill="none" stroke="#fff" stroke-width="1.2"/></svg>
        <span>info@marrowbendeyecare.com</span>
      </li>
      <li class="gap">
        <svg viewBox="0 0 16 16" aria-hidden="true"><circle cx="8" cy="8" r="7" fill="none" stroke="#0b3f63" stroke-width="1.4"/><path d="M8 3.5a3 3 0 0 0-3 3c0 2.2 3 5.5 3 5.5s3-3.3 3-5.5a3 3 0 0 0-3-3z" fill="#0b3f63"/><circle cx="8" cy="6.5" r="1.1" fill="#fff"/></svg>
        <span class="contact__address">
          <span>217-392 E Halvering Ave</span>
          <span>Vancouver BC V6R 3J8</span>
        </span>
      </li>
    </ul>
  </div>

  <svg class="wave" viewBox="0 0 730 100" preserveAspectRatio="none" aria-hidden="true">
    <path d="M0 0 C60 40 140 70 240 75 C400 80 560 48 730 80 L730 84 C560 56 400 88 240 85 C140 84 60 68 0 54 Z" fill="var(--navy)"/>
    <path d="M0 46 C80 66 160 76 260 76 C420 76 580 44 730 76 L730 100 L0 100 Z" fill="var(--brand-blue)"/>
    <path d="M0 46 C80 66 160 76 260 76 C420 76 580 44 730 76" fill="none" stroke="#ffffff" stroke-width="2.5"/>
  </svg>
</section>

<section class="card card--back" aria-label="Business card back">
  <div class="wordmark">
    <span class="wordmark__dot" aria-hidden="true"></span>
    <span>MARROW BEND</span>
    <span>EYE CARE</span>
    <span>OPTOMETRY</span>
  </div>
  <p class="website">www.marrowbendeyecare.com</p>
</section>

</body>
</html>
```